Business card design needed with water logo.

I have already designed a card at Cardwell, but prepared to pay $139 as advertised for a more professional look.
I presume it will then be available to me to order through Card Well?
The Website address needs to be large font.
I sell light weight water features at shopping centres to the public but at wholesale prices.
Need a card that is EASY TO READ, as go through literally thousands of cards as customer pick them up from my display stand.
The current logo I use is the Card Well Raincurl.
PLEASE PLACE ALL INFORMATION THAT I HAVE PROVIDED ON THE CARD
Designers keep missing out my requirements

Target Market(s)

Retail prospective customers who walk by and take a card for future reference. I go through thousands of cards so economical is a must

Industry/Entity Type

Shopping

Contact Information for Business Card

StoneGarden Company
W.A. Wholesale Agent for Pondcraftco QLD
Light Weight Fibre Glass Water Features
www.pondcraftco.com.au
See website for products but listed are RETAIL Prices
contact
MAREE HOLLOWAY
for WA Wholesale Direct Pricing
Ph: 0428596317 email: stonegardencompany@kelnet.net.au

BACK OF CARD to Read.
Stonegarden Company DISPLAYS ONLY AT SHOPPING CENTRES
..........................................................................
.........................................................................
WAREHOUSE STORAGE ONLY ( No Display)
REDPINE FREIGHTING
14 Tarrant Rd, Kewdale WA 6105 ABN 58206134872

Logo Text

StoneGarden Company

Logo styles of interest
Pictorial/Combination Logo
Requirements
Must have
• Large font to be easy to read, ALL INFORMATION On, that I specified.
This information is from my own designed card and I require the same Information just in a more professional format.

```html
<!DOCTYPE html>
<html lang="en">
<head>
<meta charset="utf-8">
<title>Stonegarden Company Business Card</title>
<link rel="stylesheet" href="https://fonts.googleapis.com/css2?family=Arimo:wght@400;700&display=swap">
<style>
  :root {
    --page: #ffffff;
    --card-blue: #33a4cc;
    --band: #7cbfd0;
    --navy: #0f3a5a;
    --bright-blue: #2f9fc9;
    --white: #ffffff;
    --edge: #2b3b45;
  }
  * { margin: 0; padding: 0; box-sizing: border-box; }
  html, body {
    width: 1200px; height: 800px; overflow: hidden;
    background: var(--page);
    font-family: "Arimo", Arial, sans-serif;
  }
  .sheet { position: relative; width: 1200px; height: 800px; }
  .card {
    position: absolute; top: 297px; width: 471px; height: 267px;
    border: 1px solid var(--edge);
    text-align: center;
  }
  .card--front { left: 103px; background: var(--card-blue); color: var(--white); }
  .card--back { left: 626px; background: var(--white); }

  .line { position: absolute; left: 0; right: 0; white-space: nowrap; }

  .brand-name {
    font-weight: 700; font-size: 43px; line-height: 1; letter-spacing: 0.5px;
  }
  .brand-name--top { top: 20px; left: -2px; }
  .brand-name--bottom { top: 60px; left: -2px; }

  .agent-band {
    position: absolute; left: 38px; top: 100px; width: 394px; height: 34px;
    background: var(--band);
    font-size: 12.5px; line-height: 14px; padding-top: 3px;
    text-transform: uppercase;
  }

  .note { font-size: 12.5px; color: var(--navy); }
  .note--retail { top: 147px; }
  .note--pricing { top: 192px; }

  .website {
    top: 162px; font-weight: 700; font-size: 22px; color: var(--navy); letter-spacing: 0.3px;
  }
  .contact {
    top: 211px; font-weight: 700; font-size: 21px; letter-spacing: 0.6px;
  }
  .contact .dash { color: var(--navy); }
  .email { top: 238px; font-size: 12.5px; }

  .back-text { font-size: 14px; line-height: 15px; }
  .back-title { top: 21px; font-weight: 700; color: var(--bright-blue); }
  .back-displays { top: 36px; font-weight: 700; color: var(--bright-blue); }
  .back-abn { top: 51px; color: var(--bright-blue); }
  .back-storage { top: 66px; color: var(--navy); }
  .back-storage strong { font-weight: 700; }
  .back-address { top: 81px; color: var(--navy); }

  .note-lines { position: absolute; left: 23px; top: 120px; }
</style>
</head>
<body>
<main class="sheet">

  <section class="card card--front" aria-label="Card front">
    <div class="line brand-name brand-name--top">STONEGARDEN</div>
    <div class="line brand-name brand-name--bottom">COMPANY</div>
    <div class="agent-band">
      W.A. Wholesale Agent for Pondcraftco<br>
      QLD Light Weight Fibre Glass Water Features
    </div>
    <div class="line note note--retail">see website for products but listed are retail prices</div>
    <div class="line website">WWW.PONDCRAFTCO.COM.AU</div>
    <div class="line note note--pricing">for W.A. Wholesale Direct Pricing</div>
    <div class="line contact">MAREE HOLLOWAY <span class="dash">-</span> PH<span class="dash">.</span> 0428596317</div>
    <div class="line email">email stonegardencompany@kelnet.net.au</div>
  </section>

  <section class="card card--back" aria-label="Card back">
    <div class="line back-text back-title">STONEGARDEN COMPANY</div>
    <div class="line back-text back-displays">DISPLAYS ONLY AT SHOPPING CENTRES</div>
    <div class="line back-text back-abn">ABN 58206134872</div>
    <div class="line back-text back-storage"><strong>WAREHOUSE STORAGE ONLY</strong> NO DISPLAY</div>
    <div class="line back-text back-address">REDPINE FREIGHTING 14 TARRANT RD, KEWDALE WA 6105</div>
    <svg class="note-lines" width="425" height="130" viewBox="0 0 425 130" aria-hidden="true">
      <g stroke="#2f9fc9" stroke-width="1.2">
        <line x1="0" y1="2" x2="424" y2="2"/>
        <line x1="0" y1="22.5" x2="424" y2="22.5"/>
        <line x1="0" y1="43" x2="424" y2="43"/>
        <line x1="0" y1="63.5" x2="424" y2="63.5"/>
        <line x1="0" y1="84" x2="424" y2="84"/>
        <line x1="0" y1="104.5" x2="424" y2="104.5"/>
        <line x1="0" y1="125" x2="424" y2="125"/>
      </g>
    </svg>
  </section>

</main>
</body>
</html>
```